VEXO requires an exciting new business card

New business card required for VEXO. We are a new market research consultancy and want our brand to be approachable and be contemporary/modern, bold, uncomplicated/simple, and use friendly and easy to read fonts.

A draft website front page is attached to give you a feel (the pictures will be improved over the coming days).

The business card will be printed on 600gsm card, full colour both sides. The card is unique in that it allows one of four colours to be placed within the seam of the card (see http://uk.tarnix.com/products/halo/business-cards.html)

The logo has been designed in yellow on white, white on yellow, yellow on black and black on yellow - please select whichever you feel most appropriate from the attached document (please use the versions with the tagline). I think my preference is yellow on white for the front, and then yellow or black as the dominant colour on the back.

Telephone numbers will be given next week as they are now being finalised.

Thanks

Target Market(s)

Professionals in large corporates, such as Marketing Managers at Bravik, Fizzor Dune, Domacore etc.

Industry/Entity Type

Market Research

Requirements
Must have
• Greg Hallow QPMR
vexo
Level 4, 17 Ember St
Quindle Park
NSW 2087
Tel: 02 XXXX XXXX
Mob: XXXX XXXXXX
Email: greg@vexomr.com.au
Web: www.vexomr.com.au

```html
<!DOCTYPE html>
<html lang="en">
<head>
<meta charset="utf-8">
<title>vexo – business card</title>
<link rel="stylesheet" href="https://fonts.googleapis.com/css2?family=Jost:ital,wght@0,400;0,500;0,600;1,400&display=swap">
<style>
  :root {
    --backdrop: #cfcbc7;
    --card-black: #0e0c0b;
    --card-white: #ffffff;
    --brand-yellow: #f2c200;
    --ink-grey: #6b6b6b;
    --ink-dark: #5a5a5a;
    --paper-white: #ffffff;
  }
  * { box-sizing: border-box; margin: 0; padding: 0; }
  html, body {
    width: 1200px;
    height: 751px;
    overflow: hidden;
  }
  body {
    position: relative;
    background: var(--backdrop);
    font-family: "Jost", "Helvetica Neue", Arial, sans-serif;
  }

  .card {
    position: absolute;
    width: 480px;
    height: 280px;
    overflow: hidden;
  }

  /* Back side */
  .card--back {
    left: 330px;
    top: 50px;
    background: var(--card-black);
  }
  .back-name {
    position: absolute;
    left: 0;
    right: 0;
    top: 95px;
    text-align: center;
    color: var(--paper-white);
    font-weight: 600;
    font-size: 84px;
    line-height: 1;
  }

  /* Front side */
  .card--front {
    left: 400px;
    top: 400px;
    background: var(--card-white);
  }
  .front-name {
    position: absolute;
    left: 40px;
    top: 50px;
    color: var(--brand-yellow);
    font-weight: 600;
    font-size: 52px;
    line-height: 1;
  }

  .person {
    position: absolute;
    left: 40px;
    top: 160px;
    color: var(--ink-grey);
  }
  .person__name {
    font-weight: 600;
    font-size: 27px;
    line-height: 1;
  }
  .person__title {
    font-style: italic;
    font-size: 12px;
    margin-top: 3px;
    padding-left: 2px;
  }

  .address {
    position: absolute;
    left: 295px;
    top: 40px;
    color: var(--ink-dark);
    font-style: normal;
    font-size: 12.5px;
    line-height: 1.3;
  }
  .address__company {
    font-weight: 600;
    font-size: 14px;
    margin-bottom: 2px;
  }
  .address__line { font-style: italic; }

  .contact {
    position: absolute;
    left: 310px;
    top: 130px;
    list-style: none;
    color: var(--ink-dark);
    font-size: 12.5px;
    line-height: 1.4;
  }
  .contact__label {
    display: inline-block;
    width: 18px;
  }
</style>
</head>
<body>

  <section class="card card--back" aria-label="Card back">
    <div class="back-name">vexo</div>
  </section>

  <section class="card card--front" aria-label="Card front">
    <div class="front-name">vexo</div>

    <div class="person">
      <div class="person__name">Greg Hallow</div>
      <div class="person__title">QPMR</div>
    </div>

    <address class="address">
      <div class="address__company">vexo</div>
      <div class="address__line">Level 4, 17 Ember St</div>
      <div class="address__line">Quindle Park</div>
      <div class="address__line">NSW 2087</div>
    </address>

    <ul class="contact">
      <li><span class="contact__label">T:</span> 02 XXXX XXXX</li>
      <li><span class="contact__label">M:</span> XXXX XXXXXX</li>
      <li><span class="contact__label">E:</span> greg@vexomr.com.au</li>
      <li><span class="contact__label">W:</span> www.vexomr.com.au</li>
    </ul>
  </section>

</body>
</html>
```